Stationery Design Project

We are looking for a full revision of our existing stationary to include within this project:

- Letterhead
- Business card
- Compliment slip

The items should be a reflection of our new website which can be found at http://www.brackenledger.co.uk/

Our logo files are included within the file brief

There are some further projects which we may approach the winning designer for as we need a revision to the front cover of our reports, a new price list and two brochures for specific target markets.

Industry/Entity Type

Business

```html
<!DOCTYPE html>
<html lang="en">
<head>
<meta charset="utf-8">
<title>Bracken Ledger — Business Card</title>
<link rel="stylesheet" href="https://fonts.googleapis.com/css2?family=Open+Sans:wght@400;600;700&family=Archivo+Black&display=swap">
<style>
  :root {
    --bg: #2b2b2d;
    --navy: #1a2a8c;
    --navy-deep: #101c66;
    --royal: #2a3fb8;
    --card-white: #f1f1f1;
    --band-grey: #dcdcdc;
    --ink: #1c1c1c;
    --muted: #333;
  }
  * { box-sizing: border-box; margin: 0; padding: 0; }
  html, body { width: 1200px; height: 900px; overflow: hidden; }
  body {
    background: var(--bg);
    font-family: "Open Sans", Arial, sans-serif;
    display: flex; flex-direction: column; align-items: center; justify-content: center;
    gap: 40px;
  }
  .card {
    position: relative; width: 700px; height: 400px; overflow: hidden;
    box-shadow: 0 12px 30px rgba(0,0,0,.45);
  }
  /* Front */
  .card--front { background: var(--card-white); }
  .card__band { position: absolute; inset: 0; }
  .bar { position: absolute; background: linear-gradient(135deg, var(--royal), var(--navy-deep)); }
  .bar--top { left: 130px; top: 0; width: 220px; height: 48px; }
  .bar--bottom { left: 0; bottom: 0; width: 200px; height: 48px; }

  .contact { position: absolute; left: 34px; top: 66px; color: var(--ink); }
  .contact__name { font-family: "Archivo Black", "Arial Black", sans-serif; font-size: 24px; line-height: 1; }
  .contact__first { color: var(--royal); }
  .contact__role { font-size: 13px; line-height: 18px; margin: 5px 0 8px; }
  .contact__line { display: flex; align-items: center; gap: 8px; font-size: 13px; line-height: 20px; white-space: nowrap; }
  .icon { width: 13px; height: 13px; flex: none; fill: none; stroke: var(--ink); stroke-width: 1.3; stroke-linejoin: round; stroke-linecap: round; }
  .icon--solid { fill: var(--ink); stroke: none; }
  .contact__company { font-family: "Archivo Black", "Arial Black", sans-serif; color: var(--royal); font-size: 13px; line-height: 18px; margin-top: 8px; }
  .contact__address { font-size: 12px; line-height: 18px; color: var(--muted); white-space: nowrap; }

  .online { position: absolute; left: 240px; top: 158px; }

  .brand-name {
    position: absolute; right: 40px; top: 78px;
    font-weight: 700; font-size: 34px; line-height: 1.2; letter-spacing: 1px; color: var(--royal);
    display: flex; align-items: center; gap: 10px; text-transform: uppercase;
  }
  .brand-name__dot { width: 12px; height: 12px; background: var(--royal); }

  /* Back */
  .card--back { background: radial-gradient(circle at 60% 40%, var(--royal), var(--navy) 55%, var(--navy-deep)); }
  .back__tab { position: absolute; left: -10px; top: 70px; width: 80px; height: 40px; background: var(--card-white); border-radius: 6px; }
  .card--back .brand-name { left: 0; right: 0; top: 172px; justify-content: center; color: #fff; font-size: 44px; }
  .card--back .brand-name__dot { background: #fff; width: 14px; height: 14px; }
</style>
</head>
<body>
  <section class="card card--front">
    <svg class="card__band" width="700" height="400" viewBox="0 0 700 400" aria-hidden="true">
      <polygon points="0,170 700,230 700,340 0,280" fill="var(--band-grey)"/>
    </svg>
    <div class="bar bar--top"></div>
    <div class="bar bar--bottom"></div>

    <div class="contact">
      <p class="contact__name"><span class="contact__first">Lucien</span>Moreau</p>
      <p class="contact__role">Managing Director</p>
      <p class="contact__line">
        <svg class="icon icon--solid" viewBox="0 0 12 12" aria-hidden="true"><path d="M2.6 0.8h2l1 2.8-1.4 1a6.5 6.5 0 0 0 3.2 3.2l1-1.4 2.8 1v2a1 1 0 0 1-1 1A10 10 0 0 1 1.6 1.8a1 1 0 0 1 1-1z"/></svg>+1 55 20 14 07</p>
      <p class="contact__line">
        <svg class="icon" viewBox="0 0 12 12" aria-hidden="true"><rect x="3" y="0.8" width="6" height="3.5"/><rect x="0.8" y="4.3" width="10.4" height="4.5" rx="0.8"/><rect x="3" y="7" width="6" height="4.2"/></svg>(1) 55 20 63 18</p>
      <p class="contact__line">
        <svg class="icon" viewBox="0 0 12 12" aria-hidden="true"><rect x="3" y="0.7" width="6" height="10.6" rx="1"/><line x1="5.2" y1="9.4" x2="6.8" y2="9.4"/></svg>+1 55 20 91 26</p>
      <p class="contact__company">Bracken Ledger Inc.</p>
      <p class="contact__address">N14 Harbour Lane, Pointe Verte, Rose-Marie, Mauritius</p>
    </div>

    <div class="online contact">
      <p class="contact__line">
        <svg class="icon" viewBox="0 0 12 12" aria-hidden="true"><circle cx="6" cy="6" r="5.2"/><ellipse cx="6" cy="6" rx="2.2" ry="5.2"/><line x1="0.8" y1="6" x2="11.2" y2="6"/></svg>www.brackenledger.co.uk</p>
      <p class="contact__line">
        <svg class="icon" viewBox="0 0 12 12" aria-hidden="true"><rect x="0.7" y="2.2" width="10.6" height="7.6" rx="0.6"/><polyline points="0.9,2.6 6,6.8 11.1,2.6"/></svg>contact@brackenledger.co.uk</p>
    </div>

    <p class="brand-name"><span class="brand-name__dot"></span>Bracken Ledger</p>
  </section>

  <section class="card card--back">
    <div class="back__tab"></div>
    <p class="brand-name"><span class="brand-name__dot"></span>Bracken Ledger</p>
  </section>
</body>
</html>
```